Hair Extension Aftercare sheet

This sheet is to give to customers regarding the aftercare of hair extensions. There should be Simple and minimal look - approx A5 size and can be folded to suit. I have attached the content and logo files for use.
We are not looking for to much artwork just clean, professional look.
All the content provided in a compact flyer format i.e
A foldable A5 pamphlet or the like, this is for packaging requirements
Please do not submit A4 layouts

Industry/Entity Type

Hair And Beauty

Requirements
Must have
• All the content provided in a compact flyer format i.e
• A foldable A5 pamphlet or the like, this is for packaging requirements
Should not have
• tacky art work or images - must be clean lines

```html
<!DOCTYPE html>
<html lang="en">
<head>
<meta charset="utf-8">
<title>Mara Whitfield Hair Extensions – Aftercare Pamphlet</title>
<link rel="stylesheet" href="https://fonts.googleapis.com/css2?family=Cormorant+Garamond:wght@500&family=Open+Sans:wght@400;700&display=swap">
<style>
  :root{
    --stage:#e3e3e3;
    --stage-alt:#d9d9d9;
    --band:#262626;
    --gold:#cfa440;
    --tan-light:#e8cf95;
    --tan-dark:#d7bd85;
    --ink:#4f4128;
    --ink-soft:#7a6845;
    --alert:#d8263f;
    --paper-edge:#f5f2ea;
  }
  *{box-sizing:border-box;margin:0;padding:0}
  html,body{width:1200px;height:1200px;overflow:hidden;background:var(--stage)}
  body{position:relative;font-family:"Open Sans",Arial,sans-serif;color:var(--ink)}

  .stage{position:absolute;display:flex;align-items:center;justify-content:center}
  .stage--cover-a{left:0;top:0;width:602px;height:496px;background:var(--stage)}
  .stage--cover-b{left:602px;top:0;width:598px;height:496px;background:var(--stage-alt)}
  .stage--inside-1{left:0;top:812px;width:408px;height:388px;background:var(--stage)}
  .stage--inside-2{left:408px;top:812px;width:397px;height:388px;background:var(--stage-alt)}
  .stage--inside-3{left:805px;top:812px;width:395px;height:388px;background:var(--stage)}

  /* brand band */
  .brand-band{position:absolute;left:0;top:496px;width:1200px;height:316px;background:var(--band);
    display:flex;flex-direction:column;align-items:center;justify-content:center;gap:8px}
  .wordmark{font-family:"Cormorant Garamond",Georgia,serif;font-weight:500;color:var(--gold);text-transform:uppercase;text-align:center;line-height:1}
  .wordmark__mark{width:14px;height:14px;background:var(--gold);margin:0 auto 18px}
  .wordmark__name{font-size:44px;letter-spacing:7px}
  .wordmark__tag{font-size:17px;letter-spacing:6px;margin-top:8px}

  /* pamphlet spreads */
  .spread{display:flex;border:2px solid var(--paper-edge);box-shadow:0 6px 14px rgba(0,0,0,.12)}
  .spread--cover{width:420px;height:290px}
  .spread--inside{width:340px;height:236px}
  .panel{position:relative;flex:1;overflow:hidden}
  .panel--back{background:var(--tan-dark)}
  .panel--front{background:var(--tan-light)}

  .cover-logo{position:absolute;inset:0;display:flex;flex-direction:column;align-items:center;justify-content:center;
    font-family:"Cormorant Garamond",Georgia,serif;font-weight:500;color:var(--ink-soft);text-transform:uppercase;text-align:center}
  .cover-logo__name{font-size:17px;letter-spacing:3px}
  .cover-logo__tag{font-size:17px;letter-spacing:3px;display:none}
  .cover-logo__sub{font-size:7px;letter-spacing:2.5px;margin-top:4px}

  .contact-box{position:absolute;left:14px;bottom:28px;width:150px;padding:8px 8px 22px;background:rgba(255,255,255,.28)}
  .contact-box li{list-style:none;display:flex;align-items:center;gap:4px;font-size:5.5px;line-height:9px;color:#2d2617}
  .icon{display:inline-block;width:5px;height:5px;background:#2d2617;flex:none}

  .page{padding:10px 9px 14px;font-size:4.4px;line-height:1.35}
  .page__brand{font-family:"Cormorant Garamond",Georgia,serif;font-weight:500;text-transform:uppercase;text-align:center;font-size:6px;letter-spacing:1px;color:var(--ink-soft);margin-bottom:6px}
  .page__title{background:rgba(255,255,255,.45);font-weight:700;text-transform:uppercase;font-size:4.8px;padding:1px 3px;margin-bottom:3px}
  .page h4{font-size:4.8px;font-weight:700;margin:3px 0 1px}
  .page p{margin-bottom:2px}
  .notice{color:var(--alert);font-weight:700;background:rgba(255,255,255,.4);padding:1px 3px;margin:3px 0;text-transform:uppercase}
  .page__url{position:absolute;bottom:5px;left:0;right:0;text-align:center;font-size:4px;color:var(--ink-soft)}
  .page__contacts li{list-style:none;display:flex;gap:3px;align-items:center;line-height:7px}
  .page__contacts .icon{width:4px;height:4px}

  .notes-title{font-family:"Cormorant Garamond",Georgia,serif;font-style:normal;font-size:8px;text-align:center;margin-bottom:6px}
  .notes-lines{height:150px;background:repeating-linear-gradient(to bottom,transparent 0 9px,rgba(120,100,60,.25) 9px 10px)}
  .notes-faint{position:absolute;left:0;right:0;top:110px;text-align:center;font-family:"Cormorant Garamond",Georgia,serif;font-weight:500;text-transform:uppercase;font-size:11px;letter-spacing:2px;color:rgba(120,100,60,.18)}
</style>
</head>
<body>

<!-- cover, view A -->
<section class="stage stage--cover-a">
  <div class="spread spread--cover">
    <div class="panel panel--back">
      <ul class="contact-box">
        <li><span class="icon"></span>Mara Whitfield Hair Extensions</li>
        <li><span class="icon"></span>MaraWhitfieldHairExtensions</li>
        <li><span class="icon"></span>info@marawhitfield.com</li>
        <li><span class="icon"></span>+61400555018</li>
      </ul>
    </div>
    <div class="panel panel--front">
      <div class="cover-logo"><span class="cover-logo__name">Mara Whitfield</span><span class="cover-logo__sub">Hair Extensions</span></div>
    </div>
  </div>
</section>

<!-- cover, view B -->
<section class="stage stage--cover-b">
  <div class="spread spread--cover">
    <div class="panel panel--back">
      <ul class="contact-box">
        <li><span class="icon"></span>Mara Whitfield Hair Extensions</li>
        <li><span class="icon"></span>MaraWhitfieldHairExtensions</li>
        <li><span class="icon"></span>info@marawhitfield.com</li>
        <li><span class="icon"></span>+61400555018</li>
      </ul>
    </div>
    <div class="panel panel--front">
      <div class="cover-logo"><span class="cover-logo__name">Mara Whitfield</span><span class="cover-logo__sub">Hair Extensions</span></div>
    </div>
  </div>
</section>

<!-- brand band -->
<section class="brand-band">
  <div class="wordmark">
    <div class="wordmark__mark"></div>
    <div class="wordmark__name">Mara Whitfield</div>
    <div class="wordmark__tag">Hair Extensions</div>
  </div>
</section>

<!-- inside spread 1 -->
<section class="stage stage--inside-1">
  <div class="spread spread--inside">
    <div class="panel panel--back page">
      <div class="page__brand">Mara Whitfield</div>
      <div class="page__title">Aftercare and maintenance guidelines</div>
      <p>Following these simple steps will keep your extensions soft, healthy and long lasting.</p>
      <h4>Brushing</h4>
      <p>Brush gently from the ends upward using a soft loop brush, twice daily.</p>
      <h4>Washing</h4>
      <p>Wash no more than twice a week with a sulphate free shampoo and cool water.</p>
      <h4>Conditioning</h4>
      <p>Apply conditioner from mid lengths to ends only, never near the bonds.</p>
      <p class="notice">Avoid oils and silicone products near the bonds.</p>
      <div class="page__url">www.marawhitfield.com</div>
    </div>
    <div class="panel panel--front page">
      <div class="page__brand">Mara Whitfield</div>
      <h4>After you washed the hair</h4>
      <p>Squeeze out excess water with a towel, do not rub or twist the lengths.</p>
      <h4>At Night</h4>
      <p>Tie hair in a loose braid or low ponytail before sleeping to prevent tangles.</p>
      <h4>Styling the hair</h4>
      <p>Always use a heat protection spray and keep tools moving.</p>
      <p class="notice">Important: never use hot styling equipment that exceeds 200 degrees</p>
      <p>Remember: regular maintenance visits keep your bonds secure and comfortable.</p>
      <div class="page__url">www.marawhitfield.com</div>
    </div>
  </div>
</section>

<!-- inside spread 2 -->
<section class="stage stage--inside-2">
  <div class="spread spread--inside">
    <div class="panel panel--back page">
      <div class="page__brand">Mara Whitfield</div>
      <h4>Sports and other activities</h4>
      <p>Tie hair up during exercise and rinse after swimming in chlorine or salt water.</p>
      <h4>Sunbathing</h4>
      <p>Cover your hair with a hat to protect colour from strong sun.</p>
      <h4>Tanning machines</h4>
      <p>Protect bonds with a towel and avoid direct heat.</p>
      <div class="page__url">www.marawhitfield.com</div>
    </div>
    <div class="panel panel--front page">
      <div class="page__brand">Mara Whitfield</div>
      <h4>General Daily Styling Guide</h4>
      <p>Start at the ends and work upward in small sections.</p>
      <p class="notice">Important: never use hot styling equipment that exceeds 200 degrees</p>
      <h4>Never brush, wash or dry the hair upside down</h4>
      <h4>Chemical Treatments</h4>
      <p>Please ask your stylist before any colour or perm service.</p>
      <h4>Colouring of extensions</h4>
      <p>Extensions may be toned but never lightened at home.</p>
      <div class="page__url">www.marawhitfield.com</div>
    </div>
  </div>
</section>

<!-- inside spread 3 -->
<section class="stage stage--inside-3">
  <div class="spread spread--inside">
    <div class="panel panel--back page">
      <div class="page__brand">Mara Whitfield</div>
      <p>Our pre-bonded extensions are crafted from ethically sourced hair for a natural finish.</p>
      <h4>For more information or questions please visit the website</h4>
      <ul class="page__contacts">
        <li><span class="icon"></span>www.marawhitfield.com</li>
        <li><span class="icon"></span>info@marawhitfield.com</li>
        <li><span class="icon"></span>+61400555018</li>
      </ul>
      <h4>Follow us on social media</h4>
      <ul class="page__contacts">
        <li><span class="icon"></span>Mara Whitfield Hair Extensions</li>
        <li><span class="icon"></span>MaraWhitfieldHairExtensions</li>
      </ul>
      <div class="page__url">www.marawhitfield.com</div>
    </div>
    <div class="panel panel--front page">
      <div class="page__brand">Mara Whitfield</div>
      <div class="notes-title">Notes</div>
      <div class="notes-lines"></div>
      <div class="notes-faint">Mara Whitfield</div>
      <div class="page__url">www.marawhitfield.com</div>
    </div>
  </div>
</section>

</body>
</html>
```